Letterhead - Quarrington Law Group

I receive a fantastic logo from you guys and I'd like to incorporate it into business cards and letterhead. I accidentally approved design No. 32361474 and contacted designer Ravindra, and Ravindra sent me the zip folder for Design No. 32361417, which I very much appreciate.
I'd like to order business cards and letterhead with Design No. 32361417 as soon as possible, but I want to make sure that you incorporate the correct design (attached). I'd also like to provide my information to add (address, phone number, email, fax) but I'm not quite sure how to do it.
The information that I would like on the business cards and letterhead is as follows:
Quarrington Law Group
Theodore K. Quarrington, Esq.
2741 Hollis Avenue, Suite 520
San Francisco, CA 94087
Office: (415) 378-6130
Fax: (415) 746-0183
ted@quarringtonlawgroup-example.com
Thanks in advance for any guidance.
Ted Quarrington
Quarrington Law Group
(415) 831-4497 (cell)

```html
<!DOCTYPE html>
<html lang="en">
<head>
<meta charset="utf-8">
<title>Quarrington Law Group – Stationery</title>
<link rel="stylesheet" href="https://fonts.googleapis.com/css2?family=Crimson+Pro:wght@400;500&display=swap">
<style>
  :root {
    --backdrop: #8c8c8c;
    --paper: #ffffff;
    --ink: #111114;
    --brand-blue: #1a8bc9;
    --brand-blue-light: #3aa3dc;
    --card-dark: #222226;
    --card-text: #f2f2f2;
  }
  * { box-sizing: border-box; margin: 0; padding: 0; }
  html, body {
    width: 1200px; height: 686px; overflow: hidden;
    background: var(--backdrop);
    font-family: "Crimson Pro", Georgia, serif;
  }
  .stage { position: relative; width: 1200px; height: 686px; }

  /* Letterhead */
  .letterhead {
    position: absolute; left: 70px; top: 32px;
    width: 440px; height: 622px;
    background: var(--paper);
    box-shadow: 0 6px 18px rgba(0,0,0,.25);
    overflow: hidden;
  }
  .letterhead__swoosh { position: absolute; inset: 0; width: 100%; height: 100%; }
  .letterhead__brand {
    position: absolute; top: 48px; right: 44px;
    text-align: right; color: var(--ink);
    font-weight: 500; font-size: 24px; line-height: 1.05;
    letter-spacing: .06em; text-transform: uppercase;
  }
  .letterhead__contact {
    position: absolute; right: 30px; bottom: 140px;
    color: var(--ink); font-size: 11.5px; line-height: 1.32;
    text-align: right; list-style: none;
  }
  .contact-line { display: flex; justify-content: flex-end; align-items: center; gap: 6px; }
  .contact-line small { font-size: .75em; }
  .icon { width: 9px; height: 9px; flex: none; fill: var(--brand-blue); }
  .icon--spacer { visibility: hidden; }

  /* Business card front */
  .card {
    position: absolute; width: 480px; height: 274px;
    box-shadow: 0 6px 16px rgba(0,0,0,.25);
    overflow: hidden;
  }
  .card--front { left: 620px; top: 54px; background: var(--card-dark); }
  .card--back { left: 620px; top: 358px; }
  .card__swoosh { position: absolute; inset: 0; width: 100%; height: 100%; }
  .card__brand {
    position: absolute; left: 56px; top: 46px; width: 170px;
    color: var(--card-text); font-weight: 500; font-size: 22px;
    line-height: 1.05; letter-spacing: .05em; text-transform: uppercase;
  }
  .card__divider {
    position: absolute; left: 246px; top: 52px; width: 1px; height: 150px;
    background: var(--card-text); opacity: .85;
  }
  .card__details {
    position: absolute; left: 264px; top: 56px; color: var(--card-text);
    font-size: 10.5px; line-height: 1.35;
  }
  .card__name { color: var(--brand-blue); font-size: 18px; line-height: 1.1; }
  .card__title { font-size: 10px; margin-bottom: 8px; }
  .card__details .contact-line { justify-content: flex-start; }
  .card__details small { color: var(--brand-blue); }

  /* Business card back */
  .card__pattern {
    position: absolute; inset: 0;
    background: linear-gradient(135deg, var(--brand-blue) 0%, var(--brand-blue-light) 60%, var(--brand-blue) 100%);
  }
  .card__back-brand {
    position: absolute; right: 40px; bottom: 30px; color: #ffffff;
    font-weight: 500; font-size: 13px; letter-spacing: .06em; text-transform: uppercase;
  }
</style>
</head>
<body>
<main class="stage">

  <!-- Letterhead -->
  <section class="letterhead">
    <svg class="letterhead__swoosh" viewBox="0 0 440 622" preserveAspectRatio="none" aria-hidden="true">
      <path d="M0,380 C40,470 150,560 440,608 L440,622 L0,622 Z" fill="var(--brand-blue)"/>
      <path d="M0,430 C70,510 190,575 440,600 L440,606 C180,578 60,515 0,440 Z" fill="var(--paper)"/>
      <path d="M90,470 C170,540 280,580 440,594 L440,600 C270,588 160,548 90,470 Z" fill="var(--ink)"/>
    </svg>

    <div class="letterhead__brand">Quarrington<br>Law Group</div>

    <ul class="letterhead__contact">
      <li class="contact-line">2741 Hollis Avenue, Suite 520<svg class="icon icon--spacer"></svg></li>
      <li class="contact-line">San Francisco, CA 94087<svg class="icon icon--spacer"></svg></li>
      <li class="contact-line">(415) 378-6130 <small>(Office)</small>
        <svg class="icon" viewBox="0 0 10 10"><path d="M2,0 L4,2.5 L3,3.5 Q4.5,6 6.5,7 L7.5,6 L10,8 L8.5,10 Q2,9 0,1.5 Z"/></svg></li>
      <li class="contact-line">(415) 746-0183 <small>(Fax)</small>
        <svg class="icon" viewBox="0 0 10 10"><rect x="0" y="3" width="10" height="7" rx="1"/><rect x="2" y="0" width="6" height="3"/></svg></li>
      <li class="contact-line">ted@quarringtonlawgroup-example.com
        <svg class="icon" viewBox="0 0 10 10"><rect x="0" y="1.5" width="10" height="7" rx="1"/></svg></li>
      <li class="contact-line">www.quarringtonlawgroup-example.com
        <svg class="icon" viewBox="0 0 10 10"><circle cx="5" cy="5" r="5"/></svg></li>
    </ul>
  </section>

  <!-- Business card, front -->
  <section class="card card--front">
    <svg class="card__swoosh" viewBox="0 0 480 274" preserveAspectRatio="none" aria-hidden="true">
      <path d="M0,120 C20,190 120,250 280,274 L0,274 Z" fill="var(--brand-blue)"/>
      <path d="M40,150 C80,210 170,255 300,274 L292,274 C165,254 80,212 40,150 Z" fill="var(--card-text)"/>
    </svg>

    <div class="card__brand">Quarrington<br>Law Group</div>
    <div class="card__divider"></div>

    <div class="card__details">
      <p class="card__name">Theodore K. Quarrington</p>
      <p class="card__title">Esq.</p>
      <p>2741 Hollis Avenue, Suite 520</p>
      <p>San Francisco, CA 94087</p>
      <p class="contact-line"><svg class="icon" viewBox="0 0 10 10"><path d="M2,0 L4,2.5 L3,3.5 Q4.5,6 6.5,7 L7.5,6 L10,8 L8.5,10 Q2,9 0,1.5 Z"/></svg>(415) 378-6130 <small>(Office)</small></p>
      <p class="contact-line"><svg class="icon" viewBox="0 0 10 10"><rect x="0" y="3" width="10" height="7" rx="1"/><rect x="2" y="0" width="6" height="3"/></svg>(415) 746-0183 <small>(Fax)</small></p>
      <p class="contact-line"><svg class="icon" viewBox="0 0 10 10"><rect x="0" y="1.5" width="10" height="7" rx="1"/></svg>ted@quarringtonlawgroup-example.com</p>
      <p class="contact-line"><svg class="icon" viewBox="0 0 10 10"><circle cx="5" cy="5" r="5"/></svg>www.quarringtonlawgroup-example.com</p>
    </div>
  </section>

  <!-- Business card, back -->
  <section class="card card--back">
    <div class="card__pattern" role="img" aria-label="Blue background with a repeating small chevron pattern"></div>
    <div class="card__back-brand">Quarrington Law Group</div>
  </section>

</main>
</body>
</html>
```